Reef Glow

sunglasses, sihoullette of body, maybe wearing a bikini or sunglasses. I am offering spray tanning, body wraps, tanning beds, stand up, body art, airbrush makeup.

Target Market(s)

I would say my target is all ages, But tanning is a seasonal business and more beauty and aging concept. and around prom time I get my most profitable business. so 18 to 21 through march and april. then 25 to 55 through april to june.

Industry/Entity Type

Makeup

Contact Information for Business Card

Phone number: 701-238-5147 Owner: Jan Porvik (Lindqvast)

Colors

Designer to choose colors to be used in the design.

Requirements
Nice to have
• Sunglasses, silouttes of body wearing sunglasses or bikini, or picture of spray gun.

```html
<!DOCTYPE html>
<html lang="en">
<head>
<meta charset="utf-8">
<title>Reef Glow — Business Card</title>
<link rel="stylesheet" href="https://fonts.googleapis.com/css2?family=Cinzel:wght@400&family=Pinyon+Script&display=swap">
<style>
  :root {
    --backdrop: #f2b8a8;
    --card: #ffffff;
    --card-edge: #e6e6e8;
    --plum: #8a2a86;
    --salmon: #e98e6f;
    --lemon: #e9e27a;
    --ink: #3b3b3b;
    --silhouette-dark: #141414;
    --silhouette-mid: #2a2a2a;
  }
  * { margin: 0; padding: 0; box-sizing: border-box; }
  html, body {
    width: 1200px;
    height: 900px;
    overflow: hidden;
    background: var(--backdrop);
  }
  .card {
    position: absolute;
    left: 75px;
    top: 150px;
    width: 1050px;
    height: 600px;
    background: var(--card);
    border: 1px solid var(--card-edge);
    box-shadow: 0 18px 40px rgba(120, 60, 50, 0.25);
    overflow: hidden;
  }
  .card__swooshes {
    position: absolute;
    inset: 0;
    width: 100%;
    height: 100%;
  }
  .card__name {
    position: absolute;
    left: 40px;
    top: 80px;
    font-family: "Pinyon Script", cursive;
    font-weight: 400;
    font-size: 110px;
    line-height: 1;
    color: var(--plum);
    white-space: nowrap;
  }
  .services {
    position: absolute;
    left: 230px;
    top: 285px;
    list-style: none;
    font-family: "Cinzel", serif;
    font-size: 25px;
    line-height: 30px;
    letter-spacing: 1px;
    color: var(--salmon);
    white-space: nowrap;
  }
  .contact {
    position: absolute;
    left: 40px;
    bottom: 24px;
    font-family: "Cinzel", serif;
    font-style: normal;
    font-size: 20px;
    line-height: 26px;
    color: var(--ink);
    white-space: nowrap;
  }
  .figure-art {
    position: absolute;
    left: 660px;
    top: 30px;
    width: 330px;
    height: 570px;
    border-radius: 110px 110px 0 0;
    background: linear-gradient(180deg, var(--silhouette-dark), var(--silhouette-mid));
  }
</style>
</head>
<body>
  <section class="card">
    <svg class="card__swooshes" viewBox="0 0 1050 600" aria-hidden="true">
      <path d="M60 258 C 300 258, 480 200, 500 110 C 512 60, 552 80, 562 250" fill="none" stroke="var(--salmon)" stroke-width="6" stroke-linecap="round"/>
      <path d="M70 235 C 60 470, 200 492, 520 492" fill="none" stroke="var(--lemon)" stroke-width="8" stroke-linecap="round"/>
    </svg>

    <h1 class="card__name">Reef Glow</h1>

    <ul class="services">
      <li>Spray Tanning</li>
      <li>Body Wraps</li>
      <li>Tanning Beds</li>
      <li>Stand Up</li>
      <li>Body Art</li>
      <li>Airbrush Makeup.</li>
    </ul>

    <address class="contact">
      <div>Phone: 701-238-5147</div>
      <div>Owner: Jan Porvik (Lindqvast)</div>
    </address>

    <div class="figure-art" role="img" aria-label="Black silhouette of a woman in a bikini and sunglasses"></div>
  </section>
</body>
</html>
```